DeskWizard.dk Frontpage design

I'm in the process of starting a It-course website, based in Denmark. The web site Url is - www.deskwizard.dk

The services are:
- Online courses (This is the main service and the most important)
- One to One courses
- Webinar

I need a frontpage design a simple design, but it must shows professionalism. I have no preference in color, but I like white space.

In Denmark the established competitors are:
- www.tasniva.dk (Biggest competitor)
- www.bramfeldt.dk/online-kurser
- www.velunda.dk

Target Market(s)

Mainly companies (B to B), but there are also a small number of private customers

Industry/Entity Type

Online it courses and one to one consulting

Number of Pages Required

1 page

Font styles to use
Sans Serif

Requirements
Must have
• A professional design, white space

```html
<!DOCTYPE html>
<html lang="da">
<head>
<meta charset="utf-8">
<title>DeskWizard.dk – Forside</title>
<link href="https://fonts.googleapis.com/css2?family=Poppins:wght@300;400;500;600&display=swap" rel="stylesheet">
<style>
:root{
  --green:#2ecc5f;
  --green-dark:#22b34f;
  --mint:#c9f5d6;
  --mint-light:#e8fbee;
  --ink:#222;
  --muted:#666;
  --line:#ddd;
  --footer:#f2f2f2;
}
*{box-sizing:border-box;margin:0;padding:0}
html,body{width:1200px;height:4010px;overflow:hidden;background:#fff}
body{font-family:'Poppins',sans-serif;color:var(--ink);position:relative}
a{color:inherit;text-decoration:none}

/* header */
.site-header{position:absolute;left:0;top:0;width:1200px;height:70px;background:#fff;border-bottom:1px solid #eee}
.brand{position:absolute;font-size:29px;font-weight:600;color:var(--green);letter-spacing:-.5px}
.main-nav{position:absolute;left:460px;top:24px;display:flex;gap:26px;font-size:14px;color:#333}
.login-btn{position:absolute;left:965px;top:16px;width:123px;height:38px;background:var(--green);color:#fff;font-size:13px;font-weight:500;display:flex;align-items:center;justify-content:center;gap:6px}

/* hero */
.hero{position:absolute;left:0;top:70px;width:1200px;height:644px;background:linear-gradient(110deg,#3a3f3d 0%,#2b302e 45%,#4a514e 70%,#1f2321 100%)}
.hero h1{position:absolute;left:110px;top:110px;width:560px;font-size:50px;line-height:65px;font-weight:600;color:#fff;white-space:nowrap}
.hero p{position:absolute;left:110px;top:382px;width:460px;font-size:13.5px;line-height:31px;color:#fff;white-space:nowrap}
.btn-outline-light{position:absolute;left:110px;top:465px;width:187px;height:57px;border:1.5px solid #fff;color:#fff;font-size:15px;display:flex;align-items:center;justify-content:center}
.play{position:absolute;left:794px;top:280px;width:84px;height:84px;border-radius:50%;background:var(--green);display:flex;align-items:center;justify-content:center}

/* section titles */
.section-title{position:absolute;left:0;width:1200px;text-align:center;font-size:42px;font-weight:500}
.section-sub{position:absolute;left:0;width:1200px;text-align:center;font-size:15px;color:#555}

/* course cards */
.course{position:absolute;top:886px;width:301px;height:418px;background:#fff;box-shadow:0 2px 12px rgba(0,0,0,.15)}
.course .thumb{position:absolute;left:10px;top:10px;width:281px;height:183px}
.course h3{position:absolute;left:19px;top:218px;font-size:15px;font-weight:500}
.course p{position:absolute;left:19px;top:250px;width:265px;font-size:12px;line-height:26px;color:#666}
.tags{position:absolute;left:19px;top:359px;display:flex;gap:7px}
.tag{width:111px;height:36px;border:1px solid var(--green);font-size:11.5px;color:#444;display:flex;align-items:center;justify-content:center}

/* why */
.why-band{position:absolute;left:0;top:1455px;width:618px;height:502px;background:var(--mint)}
.why-band h2{position:absolute;left:110px;top:112px;font-size:39px;line-height:49px;font-weight:500}
.why-band p{position:absolute;left:110px;top:216px;width:350px;font-size:13.5px;line-height:30px;color:#333}
.btn-outline-dark{position:absolute;width:187px;height:57px;border:1.5px solid #333;font-size:15px;font-weight:500;display:flex;align-items:center;justify-content:center;background:transparent}
.feature{position:absolute;width:245px;height:300px;background:#fff;box-shadow:0 2px 10px rgba(0,0,0,.12)}
.feature .icon{position:absolute;left:12px;top:20px}
.feature .rule{position:absolute;left:14px;top:128px;width:56px;height:2px;background:var(--green)}
.feature h4{position:absolute;left:22px;top:146px;font-size:15px;font-weight:500}
.feature p{position:absolute;left:22px;top:178px;width:205px;font-size:12px;line-height:26px;color:#555}
.feature .arrow{position:absolute;left:26px;top:262px}

/* services */
.service{position:absolute;top:2238px;width:318px;height:465px}
.service .photo{width:318px;height:412px}
.service .label{height:53px;background:var(--mint-light);display:flex;align-items:center;justify-content:center;font-size:15px;font-weight:500}

/* blog */
.blog-back{position:absolute;left:86px;top:2795px;width:300px;height:517px;background:var(--mint)}
.blog-photo{position:absolute;left:110px;top:2772px;width:468px;height:518px;background:linear-gradient(135deg,#cfd8dc,#8fa1a8 55%,#5e6b70);box-shadow:0 4px 14px rgba(0,0,0,.15)}
.blog h2{position:absolute;left:624px;top:2835px;font-size:33px;font-weight:500}
.blog h3{position:absolute;left:627px;top:2925px;font-size:25px;font-weight:400;color:var(--green)}
.blog .date{position:absolute;left:627px;top:2968px;font-size:13px;color:#444;display:flex;gap:6px;align-items:center}
.blog .body{position:absolute;left:627px;width:450px;font-size:13px;line-height:28px;color:#666}
.btn-green{position:absolute;width:185px;height:57px;background:var(--green);color:#fff;font-size:15px;font-weight:500;display:flex;align-items:center;justify-content:center}

/* cta */
.cta{position:absolute;left:110px;top:3388px;width:979px;height:424px;background:var(--green);box-shadow:0 3px 12px rgba(0,0,0,.2)}
.cta .frame{position:absolute;left:28px;top:27px;width:923px;height:373px;border:3px solid #fff}
.cta h2{position:absolute;left:0;top:105px;width:979px;text-align:center;color:#fff;font-size:41px;font-weight:500}
.cta p{position:absolute;left:0;top:170px;width:979px;text-align:center;color:#fff;font-size:15px;line-height:31px}
.cta .btn{position:absolute;left:396px;top:252px;width:187px;height:56px;border:1.5px solid #fff;color:#fff;font-size:15px;font-weight:500;display:flex;align-items:center;justify-content:center}

/* footer */
.site-footer{position:absolute;left:0;top:3740px;width:1200px;height:270px;background:var(--footer)}
.social{position:absolute;left:110px;top:180px;display:flex;gap:8px}
.social span{width:10px;height:10px;border-radius:50%;background:#333}
.copyright{position:absolute;left:110px;top:204px;font-size:13px;color:#333}
.foot-nav{position:absolute;right:112px;display:flex;gap:28px;color:#333}
</style>
</head>
<body>

<header class="site-header">
  <a class="brand" style="left:110px;top:13px">deskwizard</a>
  <nav class="main-nav">
    <a>Kurser</a><a>Webinar</a><a>En til En</a><a>Spørgsmål</a><a>Blog</a><a>Om</a><a>Kontakt</a>
  </nav>
  <a class="login-btn"><svg width="10" height="11" viewBox="0 0 10 11"><circle cx="5" cy="3" r="2.6" fill="#fff"/><path d="M0 11c0-3 2-5 5-5s5 2 5 5z" fill="#fff"/></svg>Log på</a>
</header>

<section class="hero" role="img" aria-label="Kontormiljø med kolleger der arbejder ved bærbare computere">
  <h1>Styrk dine it<br>kundskaber med<br>“just-in-time”<br>learning</h1>
  <p>Jeg tilbyder online kurser og webinarer med et klart fokus,<br>eller hvad med online "En til En" undervisning</p>
  <a class="btn-outline-light">Kom igang</a>
  <div class="play"><svg width="22" height="24" viewBox="0 0 22 24"><path d="M2 2l18 10L2 22z" fill="#fff"/></svg></div>
</section>

<h2 class="section-title" style="top:765px">Udvalgte kurser</h2>
<p class="section-sub" style="top:835px">Find dit næste online kursus her</p>

<article class="course" style="left:128px">
  <div class="thumb" role="img" aria-label="Person der arbejder på en bærbar computer" style="background:linear-gradient(135deg,#e9e4dc,#4a7fc2 60%,#2c3e50)"></div>
  <h3>Northsoft DataLens på én time</h3>
  <p>Er det muligt at lære Northsoft DataLens på kun én time? Nok ikke, men jeg kan give dig en introduktion.</p>
  <div class="tags"><span class="tag">DATALENS</span></div>
</article>
<article class="course" style="left:450px">
  <div class="thumb" role="img" aria-label="Nærbillede af en skærm med en programmeringsside" style="background:linear-gradient(135deg,#8c86e0,#2f3f8f 50%,#1d2b4a)"></div>
  <h3>Pylon for Celltab brugere</h3>
  <p>Hvordan kommer du som Celltab brugere i gang med at bruge Pylon</p>
  <div class="tags"><span class="tag">PYLON</span><span class="tag">CELLTAB</span></div>
</article>
<article class="course" style="left:772px">
  <div class="thumb" role="img" aria-label="Hænder ved en bærbar med diagrammer på skærmen" style="background:linear-gradient(135deg,#d8dde0,#9aa5ab 55%,#5b656b)"></div>
  <h3>Qorva Introduktion</h3>
  <p>Introduktion til Qorva programmering.</p>
  <div class="tags"><span class="tag">PYLON</span></div>
</article>

<section class="why-band">
  <h2>Hvorfor<br>DeskWizard?</h2>
  <p>Jeg har siden 1995 undervist rigtig mange glade kursister.</p>
  <a class="btn-outline-dark" style="left:110px;top:293px">Om</a>
</section>

<div class="feature" style="left:552px;top:1395px">
  <svg class="icon" width="95" height="90" viewBox="0 0 95 90"><circle cx="48" cy="42" r="42" fill="var(--mint)"/><circle cx="54" cy="22" r="11" fill="none" stroke="#333" stroke-width="2"/><path d="M6 62l18-10h18l10 5-14 4" fill="none" stroke="#333" stroke-width="2"/><path d="M38 62l20-8 10 2-30 16H10" fill="none" stroke="#333" stroke-width="2"/></svg>
  <div class="rule"></div><h4>God økonomi</h4>
  <p>Prisen på et online kursus er lavere end et fysisk kursus</p>
  <svg class="arrow" width="26" height="12" viewBox="0 0 26 12"><path d="M0 6h24M19 1l5 5-5 5" fill="none" stroke="var(--green)" stroke-width="1.6"/></svg>
</div>
<div class="feature" style="left:821px;top:1395px">
  <svg class="icon" width="95" height="90" viewBox="0 0 95 90"><circle cx="46" cy="45" r="42" fill="var(--mint)"/><path d="M48 20a16 16 0 0 1 9 29v9H39v-9a16 16 0 0 1 9-29z" fill="none" stroke="#333" stroke-width="2"/><path d="M40 64h16M42 69h12M48 0v8M22 10l6 6M74 10l-6 6M18 34h8M70 34h8" stroke="#333" stroke-width="2"/></svg>
  <div class="rule"></div><h4>Hvorfor vente</h4>
  <p>Styrk dine kompetencer på et online kursus nu</p>
  <svg class="arrow" width="26" height="12" viewBox="0 0 26 12"><path d="M0 6h24M19 1l5 5-5 5" fill="none" stroke="var(--green)" stroke-width="1.6"/></svg>
</div>
<div class="feature" style="left:552px;top:1720px">
  <svg class="icon" width="95" height="90" viewBox="0 0 95 90"><circle cx="46" cy="45" r="42" fill="var(--mint)"/><rect x="18" y="22" width="34" height="34" fill="none" stroke="#333" stroke-width="2"/><path d="M52 32h14l10 12v12H52z" fill="none" stroke="#333" stroke-width="2"/><circle cx="30" cy="60" r="6" fill="#fff" stroke="#333" stroke-width="2"/><circle cx="66" cy="60" r="6" fill="#fff" stroke="#333" stroke-width="2"/></svg>
  <div class="rule"></div><h4>Ingen rejsetid</h4>
  <p>Du slipper for spildtid og bestemmer selv hvad du skal have til frokost</p>
  <svg class="arrow" width="26" height="12" viewBox="0 0 26 12"><path d="M0 6h24M19 1l5 5-5 5" fill="none" stroke="var(--green)" stroke-width="1.6"/></svg>
</div>
<div class="feature" style="left:821px;top:1720px">
  <svg class="icon" width="95" height="90" viewBox="0 0 95 90"><circle cx="46" cy="45" r="42" fill="var(--mint)"/><path d="M44 18a22 22 0 1 0 0 44" fill="none" stroke="#333" stroke-width="2"/><circle cx="58" cy="22" r="9" fill="none" stroke="#333" stroke-width="2"/><circle cx="60" cy="52" r="10" fill="none" stroke="#333" stroke-width="2"/><circle cx="60" cy="52" r="3" fill="#333"/></svg>
  <div class="rule"></div><h4>Designed in a browser</h4>
  <p>Designing in a browser allows rapid development and saves cost.</p>
  <svg class="arrow" width="26" height="12" viewBox="0 0 26 12"><path d="M0 6h24M19 1l5 5-5 5" fill="none" stroke="var(--green)" stroke-width="1.6"/></svg>
</div>

<h2 class="section-title" style="top:2090px">Our Services</h2>
<p class="section-sub" style="top:2156px;font-size:13px;line-height:28px;width:680px;left:260px">Lorem ipsum dolor sit amet, consectetur adipiscing elit, sed do eiusmod tempor incididunt ut labore et dolore magna aliqua. Ut enim ad minim veniam, quis nostrud exercitation</p>

<div class="service" style="left:110px">
  <div class="photo" role="img" aria-label="Kursist ved en computer under et online kursus" style="background:linear-gradient(135deg,#6f5a4a,#b79f8a 50%,#8fb5cf)"></div>
  <div class="label">Online Courses</div>
</div>
<div class="service" style="left:442px">
  <div class="photo" role="img" aria-label="Mand der arbejder ved en bærbar computer" style="background:linear-gradient(135deg,#e8e8e8,#aebac4 50%,#6f7f8c)"></div>
  <div class="label">One to One courses</div>
</div>
<div class="service" style="left:772px">
  <div class="photo" role="img" aria-label="Kvinde der følger et webinar på en bærbar" style="background:linear-gradient(135deg,#d9d2c8,#8c9aa6 55%,#4c5966)"></div>
  <div class="label">Webinar</div>
</div>

<section class="blog">
  <div class="blog-back"></div>
  <div class="blog-photo" role="img" aria-label="To kolleger der samarbejder foran en computer"></div>
  <h2>Seneste blogindlæg</h2>
  <h3>Løbende sum</h3>
  <div class="date"><svg width="12" height="12" viewBox="0 0 12 12"><rect x="1" y="2" width="10" height="9" fill="none" stroke="var(--green)" stroke-width="1.4"/><path d="M1 5h10M4 0v3M8 0v3" stroke="var(--green)" stroke-width="1.4"/></svg>July 04, 2022</div>
  <p class="body" style="top:3010px">Du skal oprette en løbende sum over dine Celltab data. Det kan gøre på flere forskellige måder.</p>
  <p class="body" style="top:3092px">Jeg viser dig her 4 måder alt efter om dine data er i en tabel eller ikke.</p>
  <a class="btn-outline-dark" style="left:626px;top:3163px;width:186px">Læs artiklen</a>
  <a class="btn-green" style="left:822px;top:3163px">View More</a>
</section>

<footer class="site-footer">
  <a class="brand" style="left:110px;top:138px">deskwizard</a>
  <div class="social"><span></span><span></span><span></span></div>
  <p class="copyright">Copyright © 2022</p>
  <nav class="foot-nav" style="top:160px;font-size:15px"><a>Kurser</a><a>Webinar</a><a>En til En</a><a>Spørgsmål</a></nav>
  <nav class="foot-nav" style="top:200px;font-size:13px;gap:24px"><a>Blog</a><a>Om</a><a>Kontakt</a><a>Terms</a></nav>
</footer>

<section class="cta">
  <div class="frame"></div>
  <h2>En til En</h2>
  <p>Målrettet undervisning på det helt rigtige tidspunkt vil gøre dig<br>bedre og hurtigere til dine opgaver</p>
  <a class="btn">En til En</a>
</section>

</body>
</html>
```